Harlow Auto , a Dealership and Repair Shop in Oakvale Iowa

Harlow Auto is a repair shop and auto sales dealership that offers oil changes, alignments, tires, air conditioning work, computer diagnostics. Focused on Vantras, Marlo and Brisk. Small business with less than 10 employees. Billboard sign is in town and not the larger billboard
billboard is 8ft x 18ft

Target Market(s)

General public

Industry/Entity Type

automotive

Font styles to use
Serif
Sans Serif

Colors

Designer to choose colors to be used in the design.

Requirements
Must have
• Located 2 miles north of Oakvale. Sales and service. Phone number 319-555-0187
Nice to have
• Picture of a car or truck, or both. picture of wrench
Should not have
• Not sure

```html
<!DOCTYPE html>
<html lang="en">
<head>
<meta charset="utf-8">
<title>Harlow Auto Billboard</title>
<link rel="stylesheet" href="https://fonts.googleapis.com/css2?family=Rubik:wght@700;800;900&family=Syncopate:wght@700&family=Noto+Serif:wght@400&display=swap">
<style>
  :root {
    --page-bg: #8a8a8a;
    --paper: #ffffff;
    --brand-blue: #134f9b;
    --panel-blue: #0a55c4;
    --panel-dark: #000000;
    --accent-orange: #f5a623;
    --phone-gold: #f4b338;
    --ink: #111111;
  }
  html, body {
    margin: 0;
    padding: 0;
    width: 993px;
    height: 1200px;
    overflow: hidden;
    background: var(--page-bg);
  }
  .canvas {
    position: relative;
    width: 993px;
    height: 1200px;
  }
  .billboard {
    position: absolute;
    left: 31px;
    top: 394px;
    width: 931px;
    height: 412px;
    box-shadow: 18px 22px 26px rgba(0,0,0,0.35);
  }
  .billboard svg { display: block; width: 100%; height: 100%; }
  .business-name { font-family: "Rubik", sans-serif; font-weight: 900; fill: var(--brand-blue); }
  .location { font-family: "Rubik", sans-serif; font-weight: 800; fill: var(--ink); }
  .headline { font-family: "Syncopate", sans-serif; font-weight: 700; fill: var(--paper); }
  .tagline { font-family: "Rubik", sans-serif; font-weight: 800; fill: var(--paper); }
  .service { font-family: "Rubik", sans-serif; font-weight: 800; fill: var(--paper); }
  .phone-number { font-family: "Noto Serif", serif; fill: var(--phone-gold); }
  .make { font-family: "Rubik", sans-serif; font-weight: 800; fill: var(--ink); }
</style>
</head>
<body>
<main class="canvas">
  <section class="billboard" aria-label="Harlow Auto billboard">
    <svg viewBox="0 0 1500 665" xmlns="http://www.w3.org/2000/svg">
      <defs>
        <linearGradient id="panel-fade" x1="0" y1="1" x2="1" y2="0">
          <stop offset="0" stop-color="var(--panel-dark)"/>
          <stop offset="0.45" stop-color="#0b3a8a"/>
          <stop offset="1" stop-color="var(--panel-blue)"/>
        </linearGradient>
        <linearGradient id="band-fade" x1="0" y1="0" x2="1" y2="0">
          <stop offset="0" stop-color="var(--accent-orange)"/>
          <stop offset="0.08" stop-color="var(--panel-dark)"/>
          <stop offset="1" stop-color="var(--panel-dark)"/>
        </linearGradient>
        <linearGradient id="truck-tone" x1="0" y1="0" x2="1" y2="1">
          <stop offset="0" stop-color="#6c7076"/>
          <stop offset="1" stop-color="#3a3d41"/>
        </linearGradient>
      </defs>

      <rect class="board-paper" width="1500" height="665" fill="var(--paper)"/>
      <polygon class="corner-band" points="0,0 197,0 0,350" fill="var(--brand-blue)"/>
      <polygon class="service-panel" points="867,43 1500,43 1500,510 682,510 682,460" fill="url(#panel-fade)"/>
      <polygon class="phone-band" points="560,460 1440,460 1388,545 560,545" fill="url(#band-fade)"/>

      <rect class="truck-photo" x="0" y="280" width="590" height="385" fill="url(#truck-tone)" role="img" aria-label="Photo of a grey pickup truck, front three-quarter view"/>

      <text class="business-name" x="155" y="218" font-size="165" textLength="605" lengthAdjust="spacingAndGlyphs">Harlow</text>
      <text class="location" x="312" y="260" font-size="28" textLength="428" lengthAdjust="spacing">2 miles north of Oakvale</text>

      <text class="headline" x="862" y="172" font-size="78" textLength="408" lengthAdjust="spacingAndGlyphs">AUTO</text>
      <text class="tagline" x="847" y="218" font-size="36" textLength="584" lengthAdjust="spacing">repair and sales dealership</text>

      <g class="service-list">
        <g class="ticks" fill="var(--paper)">
          <circle cx="882" cy="290" r="9"/><circle cx="882" cy="320" r="9"/><circle cx="882" cy="350" r="9"/><circle cx="882" cy="380" r="9"/><circle cx="882" cy="410" r="9"/>
        </g>
        <g class="tick-marks" fill="none" stroke="var(--panel-dark)" stroke-width="2.5" stroke-linecap="round" stroke-linejoin="round">
          <path d="M877 290 l4 4 l6 -7"/><path d="M877 320 l4 4 l6 -7"/><path d="M877 350 l4 4 l6 -7"/><path d="M877 380 l4 4 l6 -7"/><path d="M877 410 l4 4 l6 -7"/>
        </g>
        <text class="service" x="906" y="299" font-size="24" textLength="210" lengthAdjust="spacing">OIL CHANGES</text>
        <text class="service" x="906" y="329" font-size="24" textLength="204" lengthAdjust="spacing">ALIGNMENTS</text>
        <text class="service" x="906" y="359" font-size="24" textLength="92" lengthAdjust="spacing">TIRES</text>
        <text class="service" x="906" y="389" font-size="24" textLength="409" lengthAdjust="spacing">AIR CONDITIONING WORK</text>
        <text class="service" x="906" y="419" font-size="24" textLength="402" lengthAdjust="spacing">COMPUTER DIAGNOSTICS</text>
      </g>

      <g class="phone-icon">
        <circle cx="803" cy="503" r="40" fill="var(--accent-orange)"/>
        <path d="M786 488 q-4 4 0 14 q8 16 22 22 q9 3 13 -1 l3 -4 q1 -3 -2 -5 l-7 -5 q-3 -2 -5 0 l-3 3 q-9 -4 -13 -13 l3 -3 q2 -2 0 -5 l-5 -7 q-2 -3 -5 -1 z" fill="var(--paper)"/>
        <path d="M806 482 a16 16 0 0 1 14 14 M806 473 a25 25 0 0 1 23 23" fill="none" stroke="var(--paper)" stroke-width="3" stroke-linecap="round"/>
      </g>
      <text class="phone-number" x="866" y="527" font-size="60" textLength="403" lengthAdjust="spacing">319-555-0187</text>

      <g class="makes">
        <text class="make" x="702" y="620" font-size="34" textLength="178" lengthAdjust="spacing">VANTRAS</text>
        <text class="make" x="911" y="620" font-size="34" textLength="127" lengthAdjust="spacing">MARLO</text>
        <text class="make" x="1071" y="620" font-size="34" textLength="265" lengthAdjust="spacing">BRISK</text>
        <text class="make" x="1354" y="620" font-size="26" textLength="112" lengthAdjust="spacing">TESSEL</text>
      </g>
    </svg>
  </section>
</main>
</body>
</html>
```